yourSmileCare Brookvale Business Card

Please design a two sided business card that is Elegant and Professional
Add subtle elegant patterns to suit Spot UV printing/ or raised printing

Name: Dr Marcus T. Fenwick
Qualification: BDSc (QLD)
Title: Dental Surgeon, Clinical Director
Company: yourSmileCare Brookvale
Phone: (02) 7593 2268
Address: Shop 7/18-20 Lindon Ave Brookvale 2097
email: info@yoursmilecarebrookvale.com.au
Facebook: facebook.com/yoursmilecarebrookvale

Motto:
Honest care for every smile

Description of services (not compulsory):
Preventative Dentistry | General Dentistry
Cosmetic Dentistry | Teeth Whitening
Crown and Bridge | Root Canal Therapy
Veneers | Clearvono | Orthodontics
Emergency Dental Care | After Hours

Personalised Treatment Plans
Transparent Fees

Please make sure card is elegant and professional

Target Market(s)

general population, patients,
Dental sales companies, other professions

Industry/Entity Type

Dental Clinic

Contact Information for Business Card

Name: Dr Marcus T. Fenwick
Qualification: BDSc (QLD)
Phone: (02) 7593 2268
Address: Shop 7/18-20 Lindon Ave Brookvale

Motto:

Description of services (not compulsory)

Transparent Fees

Image of dental surgery optional

Please make sure card is elegant and profession

Requirements
Must have
• Logo
• Name, Title (next to name), Business
• Phone, address, facbeook
• Must have stylish design to suit SPOT UV reflective printing
Nice to have
• Subtle elegant patterns which will have Spot UV on them when printed
• Colours to match logo colour
• Description of services
Should not have
• Small fonts that are hard to read
• DO NOT PUT IMAGES OF DENTAL INSTRUMENTS OR TEETH PLEASE

```html
<!DOCTYPE html>
<html lang="en">
<head>
<meta charset="utf-8">
<title>yourSmileCare Brookvale – Business Card</title>
<link rel="stylesheet" href="https://fonts.googleapis.com/css2?family=Open+Sans:wght@400;600;700&display=swap">
<style>
  :root {
    --green: #7dbb2c;
    --green-light: #9ccc4d;
    --green-dark: #65a11f;
    --grey-dark: #5b5c5e;
    --charcoal: #4a4b4d;
    --text: #444546;
    --white: #ffffff;
    --page: #ecebe8;
  }
  * { box-sizing: border-box; margin: 0; padding: 0; }
  html, body { width: 1200px; height: 950px; overflow: hidden; }
  body {
    background: var(--page);
    font-family: "Open Sans", Arial, sans-serif;
    color: var(--text);
    display: flex;
    flex-direction: column;
    align-items: center;
    justify-content: center;
    gap: 50px;
  }
  .card {
    position: relative;
    width: 700px;
    height: 400px;
    border-radius: 14px;
    overflow: hidden;
    box-shadow: 0 8px 24px rgba(0,0,0,.18);
  }

  /* Front */
  .card--front { background: var(--white); }
  .card--front .side-panel { position: absolute; inset: 0; }
  .brand { position: absolute; left: 44px; top: 58px; }
  .brand__name {
    font-weight: 700;
    font-size: 34px;
    line-height: 1.1;
    color: var(--charcoal);
  }
  .motto {
    font-weight: 600;
    font-size: 17px;
    color: var(--green-dark);
    margin-top: 10px;
  }
  .address {
    position: absolute; left: 44px; top: 196px;
    font-size: 17px; line-height: 1.3;
  }
  .contacts {
    position: absolute; left: 44px; top: 262px;
    list-style: none; font-size: 17px; line-height: 1.45;
  }
  .contacts li { display: flex; align-items: center; gap: 8px; }
  .contacts svg { width: 16px; height: 16px; flex: none; }
  .contacts .square { width: 14px; height: 14px; background: var(--green); border-radius: 2px; flex: none; margin: 0 1px; }
  .person {
    position: absolute; left: 612px; top: 40px;
    transform-origin: 0 0;
    transform: translateX(56px) rotate(90deg);
    color: var(--white);
    white-space: nowrap;
  }
  .person__name { font-weight: 600; font-size: 22px; }
  .person__name small { font-size: 15px; font-weight: 400; }
  .person__title { font-size: 15px; }

  /* Back */
  .card--back {
    background: linear-gradient(160deg, #6f7072 0%, var(--grey-dark) 45%, var(--charcoal) 100%);
    color: #e6e6e6;
  }
  .back__brand {
    position: absolute; left: 0; right: 0; top: 84px;
    text-align: center;
    font-weight: 700; font-size: 40px;
    color: var(--white);
  }
  .back__motto {
    position: absolute; left: 0; right: 0; top: 152px;
    text-align: center;
    font-weight: 600; font-size: 19px; color: var(--green-light);
  }
  .services {
    position: absolute; left: 40px; right: 40px; top: 204px;
    list-style: none; text-align: center;
    font-size: 15.5px; line-height: 1.6;
  }
  .back__band {
    position: absolute; left: 0; right: 0; bottom: 0; height: 22px;
    background: var(--green);
  }
</style>
</head>
<body>

<section class="card card--front" aria-label="Business card front">
  <svg class="side-panel" viewBox="0 0 700 400" preserveAspectRatio="none" aria-hidden="true">
    <defs>
      <linearGradient id="panelFill" x1="0" y1="0" x2="1" y2="1">
        <stop offset="0" stop-color="#9ccc4d"/>
        <stop offset="1" stop-color="#6eac22"/>
      </linearGradient>
    </defs>
    <path d="M590 0 L700 0 L700 400 L560 400 Z" fill="url(#panelFill)"/>
  </svg>

  <div class="brand">
    <div class="brand__name">yourSmileCare Brookvale</div>
    <div class="motto">Honest care for every smile</div>
  </div>

  <p class="address">Shop 7/18-20<br>Lindon Ave Brookvale</p>

  <ul class="contacts">
    <li>
      <svg viewBox="0 0 16 16" aria-hidden="true"><path d="M3 1.5 L6 1.5 L7 5 L5.2 6.3 C6 8 7.9 9.9 9.7 10.8 L11 9 L14.5 10 L14.5 13 C14.5 14 13.6 14.6 12.6 14.5 C6.8 13.8 2.2 9.2 1.5 3.4 C1.4 2.4 2 1.5 3 1.5 Z" fill="#7dbb2c"/></svg>
      (02) 7593 2268
    </li>
    <li>
      <svg viewBox="0 0 16 16" aria-hidden="true"><rect x="1" y="3" width="14" height="10" rx="1" fill="#7dbb2c"/><path d="M1.5 3.8 L8 9 L14.5 3.8" fill="none" stroke="#fff" stroke-width="1.3"/></svg>
      info@yoursmilecarebrookvale.com.au
    </li>
    <li><span class="square" aria-hidden="true"></span>/yoursmilecarebrookvale</li>
  </ul>

  <div class="person">
    <div class="person__name">Dr Marcus T. Fenwick <small>BDSc (QLD)</small></div>
    <div class="person__title">Dental Surgeon, Clinical Director</div>
  </div>
</section>

<section class="card card--back" aria-label="Business card back">
  <div class="back__brand">yourSmileCare Brookvale</div>
  <div class="back__motto">Honest care for every smile</div>
  <ul class="services">
    <li>Preventative Dentistry | General Dentistry | Cosmetic Dentistry</li>
    <li>Teeth Whitening | Crown and Bridge | Root Canal Therapy | Veneers</li>
    <li>Clearvono | Orthodontics | Emergency Dental Care | After Hours</li>
    <li>Personalised Treatment Plans | Transparent Fees</li>
  </ul>
  <div class="back__band"></div>
</section>

</body>
</html>
```